Glow Zone

We need a catchy flyer for a fitness class special geared to high schoolers preparing for prom / graduation / beach. Something that will catch the eye of that target audience so it should be innovative in design & look.

I have a website at www.morvadash.com that possible info could be pulled from. The specifics of the special deal are for a rate of $300.00 students can attend unlimited Zestorun & Bootcamp & Vortiplex classes to get in top shape, also receive a 30 minute home workout video, & email support weekly for a 3 month time, March thru May.

I am a great trainer, but hopeless at advertising & marketing. I want this to appeal to the age group I''m targeting. Hoping someone here can help!

```html
<!DOCTYPE html>
<html lang="en">
<head>
<meta charset="utf-8">
<title>Glow Zone – Student Special</title>
<link href="https://fonts.googleapis.com/css2?family=Allerta+Stencil&family=Arimo:wght@400;500;700&display=swap" rel="stylesheet">
<style>
  :root {
    --blue-light: #2f63d0;
    --blue-mid: #1d46a8;
    --blue-deep: #0c2470;
    --ink: #0a0a0a;
    --paper: #ffffff;
    --photo-steel: #6c6f72;
    --photo-gym: #3b3b3b;
    --photo-sea: #3f86b4;
    --photo-sky: #8fb6d8;
    --photo-sand: #b8aa96;
  }
  * { margin: 0; padding: 0; box-sizing: border-box; }
  html, body { width: 927px; height: 1200px; overflow: hidden; background: var(--blue-deep); }
  .flyer {
    position: relative; width: 927px; height: 1200px; overflow: hidden;
    background: radial-gradient(ellipse at 55% 40%, var(--blue-light) 0%, var(--blue-mid) 45%, var(--blue-deep) 100%);
    font-family: "Arimo", Arial, sans-serif; color: var(--paper);
  }

  .headline-bands { position: absolute; left: 0; top: 0; width: 927px; height: 560px; }
  .band { fill: var(--ink); }
  .band-rule { stroke: var(--paper); stroke-width: 3; fill: none; }
  .t-lead { font-family: "Arimo", Arial, sans-serif; font-weight: 700; font-size: 32px; fill: var(--paper); }
  .t-bring { font-family: "Allerta Stencil", "Arimo", sans-serif; font-size: 132px; fill: var(--paper); }
  .t-students { font-family: "Arimo", Arial, sans-serif; font-weight: 700; font-size: 72px; fill: var(--paper); }
  .t-forjust { font-family: "Arimo", Arial, sans-serif; font-weight: 700; font-size: 27px; fill: var(--paper); }
  .t-price { font-family: "Arimo", Arial, sans-serif; font-weight: 700; font-size: 102px; fill: var(--paper);
             stroke: var(--ink); stroke-width: 5; paint-order: stroke; }
  .t-price-sign { font-size: 60px; }

  .program-name {
    position: absolute; left: 642px; top: 478px;
    font-weight: 700; font-size: 30px; letter-spacing: 1px; color: var(--paper);
  }

  .offer-lead { position: absolute; left: 24px; top: 536px; font-weight: 700; font-size: 17px; }
  .offer-classes { position: absolute; left: 24px; top: 568px; font-size: 42px; font-weight: 500;
                   letter-spacing: 1.1px; white-space: nowrap; }
  .offer-details { position: absolute; right: 31px; top: 622px; font-size: 17px; font-weight: 700;
                   line-height: 26px; text-align: right; white-space: nowrap; }

  .photo-strip { position: absolute; left: 0; top: 703px; width: 927px; height: 217px; background: var(--paper); }
  .photo { position: absolute; top: 8px; height: 201px; }
  .photo-weights { left: 0; width: 273px; background: linear-gradient(160deg, var(--photo-steel), #2a2a2a 70%, #8a8d8f); }
  .photo-ring { left: 284px; width: 308px; background: linear-gradient(180deg, #9a9a9a 0%, var(--photo-gym) 45%, #141414 100%); }
  .photo-beach { left: 603px; width: 324px; background: linear-gradient(180deg, var(--photo-sky) 0%, var(--photo-sea) 50%, #7fa9c0 62%, var(--photo-sand) 100%); }

  .brand-band { position: absolute; left: 0; top: 958px; width: 927px; height: 176px; background: var(--ink); }
  .brand-rule { position: absolute; left: 0; width: 927px; height: 3px; background: var(--paper); }
  .brand-rule.top { top: 16px; }
  .brand-rule.bottom { top: 162px; }
  .brand-name {
    position: absolute; left: 0; top: 30px; width: 927px; text-align: center;
    font-family: "Arimo", Arial, sans-serif; font-weight: 700; font-size: 124px; line-height: 124px;
    letter-spacing: 14px; color: var(--paper);
  }

  .trainer-tag { position: absolute; left: 260px; top: 1105px; width: 407px; height: 69px; }
  .tag-shape { fill: var(--paper); stroke: var(--ink); stroke-width: 4; }
  .t-trainer { font-family: "Arimo", Arial, sans-serif; font-weight: 700; font-size: 40px; fill: var(--ink); }
</style>
</head>
<body>
<main class="flyer">

  <svg class="headline-bands" viewBox="0 0 927 560" aria-label="Be prepared to bring it, students! For just $300">
    <g transform="rotate(-7)">
      <rect class="band" x="-60" y="60" width="1160" height="180"/>
      <line class="band-rule" x1="-60" y1="251" x2="1100" y2="251"/>
      <text class="t-lead" x="53" y="112">Be prepared to</text>
      <text class="t-bring" x="120" y="222" textLength="458" lengthAdjust="spacingAndGlyphs">BRING IT</text>

      <line class="band-rule" x1="-60" y1="274" x2="820" y2="274"/>
      <polygon class="band" points="-60,284 815,284 800,380 -60,380"/>
      <line class="band-rule" x1="-60" y1="390" x2="1100" y2="390"/>
      <text class="t-students" x="150" y="362" textLength="434" lengthAdjust="spacingAndGlyphs">STUDENTS!</text>

      <polygon class="band" points="189,430 1100,430 1100,483 155,483"/>
      <line class="band-rule" x1="150" y1="493" x2="1100" y2="493"/>
      <text class="t-forjust" x="330" y="468">for just</text>
      <text class="t-price" x="515" y="489"><tspan class="t-price-sign" dy="-38">$</tspan><tspan dy="38">300</tspan></text>
    </g>
  </svg>

  <div class="program-name">VORTIPLEX</div>

  <p class="offer-lead">you can attend</p>
  <h2 class="offer-classes">unlimited Zestorun &amp; Bootcamp &amp; Vortiplex</h2>
  <p class="offer-details">classes to get in top shape, also receive a 30 minute home workout<br>video, &amp; email support weekly for a 3 month time, March thru May.</p>

  <section class="photo-strip">
    <div class="photo photo-weights" role="img" aria-label="Rack of dumbbells in a gym"></div>
    <div class="photo photo-ring" role="img" aria-label="Athlete training in a boxing ring"></div>
    <div class="photo photo-beach" role="img" aria-label="Sunny beach with blue sea and sky"></div>
  </section>

  <section class="brand-band">
    <div class="brand-rule top"></div>
    <h1 class="brand-name">GLOW ZONE</h1>
    <div class="brand-rule bottom"></div>
  </section>

  <svg class="trainer-tag" viewBox="0 0 407 69" aria-label="By Delphine">
    <polygon class="tag-shape" points="28,3 379,3 404,34.5 379,66 28,66 3,34.5"/>
    <text class="t-trainer" x="203.5" y="49" text-anchor="middle">BY DELPHINE</text>
  </svg>

</main>
</body>
</html>
```